Menu board for car wash

I need to have a menu board designed for my car wash. I would like for it to replicate the attached graphics of other menu boards other car washes are using. The menu board will be printed locally and be cut out with a router. I want the menu board to clearly show what they are buying and promote buying the top wash package. I also want "the Works" package to show that you can buy a monthly plan for $23.95 and receive this wash unlimited times per month. I have attached my menu that i have now (Kellingtonmenu). I would like for this new menu to have the same wording as the previous menu for the wash packages. The only addition is a new wash package "Summit Sparkle" which is now the top wash package. The new menu i would like to have going vertical and I would like my logo on the top. This menu would be 8' high and 4'wide.

Target Market(s)

Looking to have this menu be attractive and inviting. The top package should stand out the most and the lowest package should barely be noticeable ( basic wash)
I am targeting customer from the ages of 16-65 years old.

Industry/Entity Type

Automotive

Font styles to use
Serif
Sans Serif
Decorative
Other font styles liked:
• any font that flows with the design

Colors

Designer to choose colors to be used in the design.

Requirements
Must have
• This menu will be die cut out. It must fit in a 8' x 4' vertical art board.
• The wash packages will need to go from top to bottom
• They should be listed as follows
• Summit Sparkle $18
• The Works $13 ( also add Unlimited for $23.95)
• Deluxe $10
• Basic $8
• I would like to have an extras section also added just like my original menu. This can be at the bottom of the menu If you have any cool graphics that go with my theme or washes please feel free.
• The new Summit Sparkle wash will have the following included:
• Presoak
• Bug Treatment
• wheel cleaner
• Undercarriage wash
• Triple Foam Polish
• Clear Coat Protectant
• Hot Wax Treatment ( you can use graphic that is on my old menu for this item)
• Tire Shine ( You can use the Storm Glide logo)
• Hand Towel Dried
Nice to have
• Incorporate my business hours also on the menu
• the hours are:
• Monday-Saturday 8:00 Am-6:00 Pm
• Sunday 8:00 Am-5:00 Pm
• Weather may effect these hours
Should not have
• Text should be clearly visable so anyone car read it easily

```html
<!DOCTYPE html>
<html lang="en">
<head>
<meta charset="utf-8">
<title>Kellington's Summit Car Wash – Menu Board</title>
<link rel="stylesheet" href="https://fonts.googleapis.com/css2?family=Archivo+Black&family=Luckiest+Guy&family=Lilita+One&family=Rubik:wght@400;500;700;800&display=block">
<style>
  :root {
    --backdrop: #7b7b7b;
    --sky: #9fd8f2;
    --sky-deep: #5ec3ec;
    --red: #e8333a;
    --yellow: #f5d530;
    --cream: #fbeaa8;
    --white: #ffffff;
    --ink: #1b1b1b;
  }
  * { margin: 0; padding: 0; box-sizing: border-box; }
  html, body { width: 720px; height: 1200px; overflow: hidden; background: var(--backdrop); }
  .canvas { position: relative; width: 720px; height: 1200px; overflow: hidden; font-family: "Rubik", sans-serif; }
  .abs { position: absolute; }

  .board-bg { left: 92px; top: 80px; width: 518px; height: 1040px;
    background: linear-gradient(180deg, var(--sky) 0%, #c7ebf9 55%, var(--sky-deep) 100%); }

  .logo-panel { left: 94px; top: 82px; width: 514px; height: 182px; background: var(--yellow);
    border: 6px solid var(--red); border-radius: 26px; box-shadow: inset 0 0 0 4px var(--sky); }
  .logo-name { width: 100%; text-align: center; font-family: "Lilita One", sans-serif; color: var(--red); line-height: 1; }
  .logo-name .top { display: block; font-size: 46px; margin-top: 18px; }
  .logo-name .main { display: block; font-size: 92px; margin-top: 2px; }

  .shape { left: 0; top: 0; }

  .summit-title { left: 104px; top: 290px; font-family: "Luckiest Guy", "Lilita One", sans-serif; font-weight: 400; color: var(--yellow); line-height: 1; }
  .summit-title .big { display: block; font-size: 58px; letter-spacing: 1px; }
  .summit-title .small { display: block; font-size: 28px; margin-left: 144px; margin-top: -2px; }

  .feature-list { left: 130px; top: 372px; list-style: none; }
  .feature-list li { display: flex; align-items: center; gap: 9px; height: 23px;
    font-size: 19px; font-weight: 700; color: var(--cream); }
  .feature-list svg { width: 14px; height: 14px; flex: none; }

  .price { display: flex; align-items: center; justify-content: center; border-radius: 50%;
    font-family: "Archivo Black", sans-serif; }
  .price-summit { left: 430px; top: 310px; width: 188px; height: 188px; background: var(--yellow);
    border: 5px solid var(--white); font-size: 78px; color: var(--ink); }

  .wax-art { left: 200px; top: 540px; width: 120px; height: 58px; border-radius: 8px;
    background: radial-gradient(circle at 50% 60%, var(--yellow) 0%, #f0b62a 70%); }
  .wax-label { left: 150px; top: 597px; width: 220px; text-align: center; font-size: 19px; font-weight: 700; color: var(--yellow); white-space: nowrap; }
  .tire-brand { left: 376px; top: 562px; width: 132px; text-align: center; font-size: 16px; font-weight: 800; color: var(--white); white-space: nowrap; }
  .tire-brand::before { content: ""; display: inline-block; width: 9px; height: 9px; border-radius: 50%; background: var(--white); margin-right: 5px; vertical-align: 1px; }
  .tire-label { left: 376px; top: 597px; width: 132px; text-align: center; font-size: 19px; font-weight: 700; color: var(--white); white-space: nowrap; }

  .works-title { left: 94px; top: 670px; font-family: "Luckiest Guy", "Lilita One", sans-serif; font-weight: 400; font-size: 32px; color: var(--red); letter-spacing: 1px; }
  .works-copy { left: 104px; top: 720px; color: var(--ink); line-height: 1.15; }
  .works-copy .plan { font-size: 17px; font-weight: 700; }
  .works-copy .plan b { color: var(--red); }
  .works-copy .receive { font-size: 14px; font-weight: 500; }
  .works-copy .unlimited { font-size: 17px; font-weight: 800; color: var(--red); margin-top: 4px; }
  .price-works { left: 382px; top: 650px; width: 128px; height: 128px; background: var(--red);
    border: 5px solid var(--white); font-size: 48px; color: var(--white); z-index: 2; }

  .tier-name { font-family: "Archivo Black", sans-serif; line-height: 1; }
  .deluxe-name { left: 106px; top: 832px; font-size: 50px; color: var(--yellow); }
  .price-deluxe { left: 328px; top: 808px; width: 84px; height: 84px; background: var(--yellow);
    border: 4px solid var(--white); font-size: 30px; color: var(--ink); }
  .basic-name { left: 106px; top: 930px; font-size: 46px; color: var(--red); }
  .price-basic { left: 305px; top: 917px; width: 74px; height: 74px; background: var(--red);
    border: 4px solid var(--white); font-size: 26px; color: var(--white); }

  .hours { left: 80px; top: 1008px; width: 340px; height: 104px; background: var(--red);
    border: 4px solid var(--yellow); border-radius: 10px; color: var(--white); padding: 4px 22px 0; }
  .hours h2 { text-align: center; font-size: 23px; font-weight: 700; }
  .hours dl { display: grid; grid-template-columns: 146px 1fr; font-size: 15px; line-height: 1.2; margin-top: 2px; }
  .hours .note { text-align: center; font-size: 13px; margin-top: 6px; }

  .extras { left: 426px; top: 1008px; width: 86px; height: 104px; background: var(--yellow);
    border: 4px solid var(--red); border-radius: 10px; color: var(--ink); text-align: center;
    display: flex; flex-direction: column; justify-content: center; gap: 4px; }
  .extras h2 { font-size: 16px; font-weight: 800; color: var(--red); }
  .extras p { font-size: 12px; font-weight: 700; line-height: 1.15; }

  .attendant-art { left: 520px; top: 604px; width: 146px; height: 516px; border-radius: 56px 56px 18px 18px;
    background: linear-gradient(180deg, #3e8fa8 0%, #f0a531 28%, #2f9ab6 52%, #257f9a 100%); }
</style>
</head>
<body>
<main class="canvas">
  <div class="abs board-bg"></div>

  <header class="abs logo-panel">
    <h1 class="logo-name"><span class="top">Kellington's Summit</span><span class="main">Car Wash</span></h1>
  </header>

  <svg class="abs shape" width="720" height="1200" viewBox="0 0 720 1200" aria-hidden="true">
    <path d="M84 280 H620 Q636 280 634 298 L600 624 Q598 636 586 636 H118 Q106 636 104 624 L68 298 Q66 280 84 280 Z"
          fill="var(--red)" stroke="var(--yellow)" stroke-width="6"/>
    <path d="M72 648 H628 Q642 648 638 662 L614 790 Q612 800 600 800 H100 Q88 800 86 790 L64 662 Q62 648 72 648 Z"
          fill="var(--yellow)" stroke="var(--red)" stroke-width="6"/>
    <path d="M64 812 H638 L620 896 H86 Z" fill="var(--red)" stroke="var(--yellow)" stroke-width="6" stroke-linejoin="round"/>
    <path d="M64 912 H638 L620 998 H86 Z" fill="var(--yellow)" stroke="var(--red)" stroke-width="6" stroke-linejoin="round"/>
  </svg>

  <h2 class="abs summit-title"><span class="big">SUMMIT</span><span class="small">SPARKLE</span></h2>
  <ul class="abs feature-list">
    <li><svg viewBox="0 0 14 14"><circle cx="7" cy="7" r="6" fill="none" stroke="var(--yellow)" stroke-width="1.5"/><path d="M3.5 7 L6 9.5 L12 2.5" fill="none" stroke="var(--yellow)" stroke-width="2"/></svg>Presoak</li>
    <li><svg viewBox="0 0 14 14"><circle cx="7" cy="7" r="6" fill="none" stroke="var(--yellow)" stroke-width="1.5"/><path d="M3.5 7 L6 9.5 L12 2.5" fill="none" stroke="var(--yellow)" stroke-width="2"/></svg>Bug Treatment</li>
    <li><svg viewBox="0 0 14 14"><circle cx="7" cy="7" r="6" fill="none" stroke="var(--yellow)" stroke-width="1.5"/><path d="M3.5 7 L6 9.5 L12 2.5" fill="none" stroke="var(--yellow)" stroke-width="2"/></svg>wheel cleaner</li>
    <li><svg viewBox="0 0 14 14"><circle cx="7" cy="7" r="6" fill="none" stroke="var(--yellow)" stroke-width="1.5"/><path d="M3.5 7 L6 9.5 L12 2.5" fill="none" stroke="var(--yellow)" stroke-width="2"/></svg>Undercarriage wash</li>
    <li><svg viewBox="0 0 14 14"><circle cx="7" cy="7" r="6" fill="none" stroke="var(--yellow)" stroke-width="1.5"/><path d="M3.5 7 L6 9.5 L12 2.5" fill="none" stroke="var(--yellow)" stroke-width="2"/></svg>Triple Foam Polish</li>
    <li><svg viewBox="0 0 14 14"><circle cx="7" cy="7" r="6" fill="none" stroke="var(--yellow)" stroke-width="1.5"/><path d="M3.5 7 L6 9.5 L12 2.5" fill="none" stroke="var(--yellow)" stroke-width="2"/></svg>Clear Coat Protectant</li>
    <li><svg viewBox="0 0 14 14"><circle cx="7" cy="7" r="6" fill="none" stroke="var(--yellow)" stroke-width="1.5"/><path d="M3.5 7 L6 9.5 L12 2.5" fill="none" stroke="var(--yellow)" stroke-width="2"/></svg>Hand Towel Dried</li>
  </ul>
  <div class="abs price price-summit">$18</div>

  <div class="abs wax-art" role="img" aria-label="Illustration of a yellow car in front of a rising sun"></div>
  <div class="abs wax-label">Hot Wax Treatment</div>
  <div class="abs tire-brand">Storm Glide</div>
  <div class="abs tire-label">TIRE SHINE</div>

  <h2 class="abs works-title">THE WORKS</h2>
  <div class="abs works-copy">
    <p class="plan">Buy A Monthly Plan For <b>$23.95</b></p>
    <p class="receive">and receive this wash</p>
    <p class="unlimited">UNLIMITED TIMES PER MONTH</p>
  </div>

  <h2 class="abs tier-name deluxe-name">Deluxe</h2>
  <div class="abs price price-deluxe">$10</div>

  <h2 class="abs tier-name basic-name">Basic</h2>
  <div class="abs price price-basic">$8</div>

  <section class="abs hours">
    <h2>BUSINESS HOURS</h2>
    <dl>
      <dt>Monday-Saturday</dt><dd>8:00 Am-6:00 Pm</dd>
      <dt>Sunday</dt><dd>8:00 Am-5:00 Pm</dd>
    </dl>
    <p class="note">(Weather may effect these hours)</p>
  </section>

  <section class="abs extras">
    <h2>EXTRAS</h2>
    <p>Ask Our Attendant</p>
  </section>

  <div class="abs attendant-art" role="img" aria-label="Cartoon car wash attendant in cap and overalls holding a pressure washer wand"></div>
  <div class="abs price price-works">$13</div>
</main>
</body>
</html>
```